Asphalt Paving Specialists Business Cards

Our company is TREVIN ASPHALT. We need a business cards two of our asphalt paving team members. We're asphalt specialists.
I need two made up please. The details on the front of the each business card i would like please is as follows.
Address is 87 Marrowby St, Clontarf, QLD, 4019.

Company Director
Gordon Pelliway
gord@trevinpave.com.au
04 58 736 042
www.trevinpave.com.au

Supervisor
Curtis Vonnegard
curtis@trevinpave.com.au
0462 873 105
www.trevinpave.com.au

We do all aspects of Asphalt Paving. Specific Services include - Driveways, Carparks & sub-divisions. All Roads. Repairs and Maintenance.

We provide free quotes!

I dont have a certain way i want them to look so im open to all designs :)

** I have uploaded our logo for the TREVIN ASPHALT. HOWEVER, CAN YOU PLEASE GET RID OF THE ( PTY LTD )

Thank you
Renata Fulch
TREVIN ASPHALT

Target Market(s)

Home owners and Business Owners

Contact Information for Business Card

Asphalt Paving Specialists. All aspects of Asphalt. Residential, Commercial & Industrial. Based in Brisbane.

Font styles to use
Sans Serif

Colors

Designer to choose colors to be used in the design.

Requirements
Nice to have
• maybe an image of a driveway? or Asphalt?

```html
<!DOCTYPE html>
<html lang="en">
<head>
<meta charset="utf-8">
<title>Trevin Asphalt Business Card</title>
<link href="https://fonts.googleapis.com/css2?family=Roboto:wght@400;500;700&family=Roboto+Condensed:wght@700&display=swap" rel="stylesheet">
<style>
  :root {
    --page-bg: #e4e4e4;
    --card-white: #ffffff;
    --sky-blue: #00b2ee;
    --sky-glow: #bfe9fb;
    --ink: #111111;
    --asphalt-dark: #2a2a2a;
    --asphalt-mid: #4a4a4a;
    --text-light: #ffffff;
    --rule: rgba(255,255,255,0.85);
  }
  * { margin: 0; padding: 0; box-sizing: border-box; }
  html, body { width: 1125px; height: 1200px; overflow: hidden; }
  body {
    background: var(--page-bg);
    position: relative;
    font-family: "Roboto", Arial, sans-serif;
    color: var(--ink);
  }
  .card {
    position: absolute;
    left: 166px;
    width: 800px;
    height: 456px;
    overflow: hidden;
  }
  .card-front { top: 103px; background: var(--card-white); }
  .card-back { top: 619px; }

  .front-brand {
    position: absolute;
    left: 0; top: 0;
    width: 427px; height: 456px;
    display: flex; align-items: center; justify-content: center;
  }
  .brand-name {
    font-family: "Roboto", Arial, sans-serif;
    font-weight: 700;
    font-size: 34px;
    letter-spacing: 1px;
    color: var(--ink);
    display: flex; align-items: center; gap: 12px;
  }
  .brand-mark {
    width: 22px; height: 22px;
    border-radius: 50%;
    background: var(--sky-blue);
  }

  .front-details {
    position: absolute;
    left: 427px; top: 0;
    width: 373px; height: 456px;
    background: radial-gradient(circle at 48% 45%, var(--sky-glow) 0%, var(--sky-blue) 55%, var(--sky-blue) 100%);
  }
  .sparkle {
    position: absolute;
    left: 370px; top: 60px;
    width: 110px; height: 70px;
    background: radial-gradient(ellipse at center, rgba(255,255,255,0.95) 0%, rgba(255,255,255,0.4) 25%, rgba(255,255,255,0) 65%);
  }
  .person-name {
    position: absolute;
    left: 70px; top: 78px;
    font-family: "Roboto Condensed", "Arial Narrow", sans-serif;
    font-weight: 700;
    font-size: 29px;
    color: var(--ink);
  }
  .person-title {
    position: absolute;
    left: 71px; top: 113px;
    font-size: 20px;
    font-weight: 500;
    letter-spacing: 0.3px;
    color: var(--ink);
  }
  .contact-list {
    position: absolute;
    left: 70px; top: 268px;
    list-style: none;
  }
  .contact-list li {
    display: flex; align-items: center; gap: 12px;
    font-size: 19px;
    height: 25.5px;
    color: var(--ink);
  }
  .contact-list svg { width: 17px; height: 17px; flex: none; }

  .asphalt-surface {
    position: absolute; inset: 0;
    background: radial-gradient(circle at 50% 45%, var(--asphalt-mid) 0%, var(--asphalt-dark) 100%);
  }
  .back-brand {
    position: absolute;
    left: 0; right: 0; top: 150px;
    text-align: center;
    font-weight: 700;
    font-size: 40px;
    letter-spacing: 2px;
    color: var(--text-light);
  }
  .back-tagline {
    position: absolute;
    left: 0; right: 0; top: 340px;
    text-align: center;
    font-size: 18px;
    color: var(--text-light);
  }
  .services-heading {
    position: absolute;
    left: 121px; width: 579px; top: 366px;
    display: flex; align-items: center; gap: 4px;
    font-size: 18px;
    color: var(--text-light);
  }
  .services-heading::before, .services-heading::after {
    content: ""; flex: 1; height: 1px; background: var(--rule);
  }
  .services-list {
    position: absolute;
    left: 0; right: 0; top: 391px;
    text-align: center;
    font-size: 18px;
    color: var(--text-light);
  }
</style>
</head>
<body>
  <section class="card card-front">
    <div class="front-brand">
      <div class="brand-name"><span class="brand-mark"></span>TREVIN ASPHALT</div>
    </div>
    <div class="front-details">
      <div class="sparkle" role="img" aria-label="Small light flare ornament"></div>
      <h1 class="person-name">Gordon Pelliway</h1>
      <p class="person-title">COMPANY DIRECTOR</p>
      <ul class="contact-list">
        <li>
          <svg viewBox="0 0 24 24" aria-hidden="true"><path fill="#111" d="M6.6 10.8a15.1 15.1 0 0 0 6.6 6.6l2.2-2.2a1 1 0 0 1 1-.25 11.4 11.4 0 0 0 3.6.57 1 1 0 0 1 1 1V20a1 1 0 0 1-1 1A17 17 0 0 1 3 4a1 1 0 0 1 1-1h3.5a1 1 0 0 1 1 1c0 1.25.2 2.45.57 3.57a1 1 0 0 1-.25 1z"/></svg>
          04 58 736 042
        </li>
        <li>
          <svg viewBox="0 0 24 24" aria-hidden="true"><rect x="3" y="6" width="18" height="12" fill="none" stroke="#111" stroke-width="2"/><path d="M3 6l9 7 9-7" fill="none" stroke="#111" stroke-width="2"/></svg>
          gord@trevinpave.com.au
        </li>
        <li>
          <svg viewBox="0 0 24 24" aria-hidden="true"><circle cx="12" cy="12" r="9.5" fill="#111"/><path d="M7 8c2 0 3 1 3 2s-2 1-2 3 2 2 2 4M15 5c-1 2 1 3 2 3s2 2 1 4" fill="none" stroke="#00b2ee" stroke-width="1.6"/></svg>
          www.trevinpave.com.au
        </li>
      </ul>
    </div>
  </section>

  <section class="card card-back">
    <div class="asphalt-surface" role="img" aria-label="Close-up texture of dark asphalt paving"></div>
    <div class="back-brand">TREVIN ASPHALT</div>
    <p class="back-tagline">We do all aspects of Asphalt Paving.</p>
    <p class="services-heading">Specific Services</p>
    <p class="services-list">Driveways • Carparks &amp; sub-divisions • All Roads • Repairs &amp; Maintenance.</p>
  </section>
</body>
</html>
```